Graphic Design of Business Process

We require an eye-catching, sophisticated design of 2 business processes (attached), that will be used digitally AND for print (to be put on walls in our office).

The basic layout is attached. We require a creative, professional designer to re-design these so that they look appealing but still able to grasp all the information.

We will require vector files and editable project files for final delivery. You may refer to our website (kitefieldmedia.com.au) for an indication of our brand.

If you have any questions, please ask.

Thank you.

```html
<!DOCTYPE html>
<html lang="en">
<head>
<meta charset="utf-8">
<title>Sales Content Funnel</title>
<link rel="stylesheet" href="https://fonts.googleapis.com/css2?family=Archivo+Black&family=Montserrat:wght@300;500;600;700;800&family=Open+Sans:wght@400;600;700&family=Open+Sans+Condensed:wght@700&display=swap">
<style>
  :root {
    --red: #e2332b;
    --yellow: #ffea00;
    --maroon: #761510;
    --amber: #a65817;
    --black: #050505;
    --white: #ffffff;
    --ink: #111111;
  }
  html, body {
    margin: 0;
    padding: 0;
    width: 1200px;
    height: 1200px;
    overflow: hidden;
    background: var(--white);
  }
  .poster { display: block; width: 1200px; height: 1200px; }
  .title-main { font-family: "Archivo Black", sans-serif; fill: var(--red); }
  .title-sub { font-family: "Montserrat", sans-serif; font-weight: 600; fill: var(--ink); }
  .rule { stroke: var(--ink); stroke-width: 4; }
  .stage-name { font-family: "Montserrat", sans-serif; font-weight: 800; }
  .stage-task { font-family: "Montserrat", sans-serif; font-weight: 500; }
  .stage-note { font-family: "Open Sans", sans-serif; font-weight: 400; }
  .stage-note--bold { font-family: "Open Sans", sans-serif; font-weight: 700; letter-spacing: -0.6px; }
  .on-red { fill: var(--white); }
  .on-yellow { fill: var(--ink); }
  .band-label { font-family: "Open Sans", sans-serif; font-weight: 600; fill: var(--white); }
  .site-url { font-family: "Open Sans", sans-serif; font-weight: 700; fill: var(--white); letter-spacing: 0.5px; }
  .flow-arrow { stroke: var(--white); stroke-width: 3; fill: none; }
</style>
</head>
<body>
<svg class="poster" viewBox="148 73 1222 1222" xmlns="http://www.w3.org/2000/svg">
  <!-- header -->
  <rect class="header" x="148" y="73" width="1222" height="227" fill="var(--white)"/>
  <text class="title-main" x="773" y="197" font-size="80" text-anchor="middle" textLength="735" lengthAdjust="spacingAndGlyphs">SALES CONTENT</text>
  <line class="rule" x1="408" y1="237" x2="628" y2="237"/>
  <line class="rule" x1="918" y1="237" x2="1128" y2="237"/>
  <text class="title-sub" x="773" y="254" font-size="54" text-anchor="middle" textLength="246" lengthAdjust="spacingAndGlyphs">FUNNEL</text>

  <!-- dark field -->
  <rect class="field" x="148" y="300" width="1222" height="995" fill="var(--black)"/>

  <!-- extruded bands -->
  <polygon class="band band--awareness" points="1053,313 1370,705 1370,1010 953,494" fill="var(--maroon)"/>
  <polygon class="band band--consideration" points="940,510 1370,1042 1370,1295 1342,1295 832,697" fill="var(--amber)"/>
  <polygon class="band band--action" points="823,713 1330,1295 603,1095" fill="var(--maroon)"/>

  <!-- funnel stages -->
  <polygon class="stage stage--awareness" points="150,313 1053,313 949,494 255,494" fill="var(--red)"/>
  <polygon class="stage stage--consideration" points="264,510 940,510 832,697 372,697" fill="var(--yellow)"/>
  <polygon class="stage stage--action" points="382,713 823,713 603,1095" fill="var(--red)"/>

  <!-- awareness -->
  <polygon class="chevron" points="265,347 290,347 315,370 290,393 265,393 290,370" fill="var(--white)"/>
  <text class="stage-name on-red" x="343" y="388" font-size="58" textLength="413" lengthAdjust="spacingAndGlyphs">AWARENESS</text>
  <text class="stage-task on-red" x="370" y="430" font-size="26" textLength="387" lengthAdjust="spacingAndGlyphs">IDENTIFY PROBLEM/NEED</text>
  <text class="stage-note on-red" x="383" y="460" font-size="16">-Aspirational</text>
  <text class="stage-note on-red" x="383" y="481" font-size="16">- Market The Outcome Not Product</text>

  <!-- consideration -->
  <polygon class="chevron" points="328,547 356,547 383,570 356,593 328,593 355,570" fill="var(--ink)"/>
  <text class="stage-name on-yellow" x="387" y="587" font-size="50" textLength="478" lengthAdjust="spacingAndGlyphs">CONSIDERATION</text>
  <text class="stage-task on-yellow" x="427" y="625" font-size="27" textLength="384" lengthAdjust="spacingAndGlyphs">EVALUATE ALTERNATIVES</text>
  <text class="stage-note--bold on-yellow" x="447" y="657" font-size="16">-why Is This Solution Better Than Others</text>
  <text class="stage-note--bold on-yellow" x="447" y="678" font-size="16">- How Is This Provider Going To Solve My Need</text>

  <!-- action / decision -->
  <polygon class="chevron" points="443,741 468,741 493,764 468,787 443,787 468,764" fill="var(--white)"/>
  <text class="stage-name on-red" x="505" y="770" font-size="46" textLength="222" lengthAdjust="spacingAndGlyphs">ACTION/</text>
  <text class="stage-name on-red" x="505" y="817" font-size="46" textLength="240" lengthAdjust="spacingAndGlyphs">DECISION</text>
  <text class="stage-task on-red" x="505" y="857" font-size="24" font-weight="300" textLength="222" lengthAdjust="spacingAndGlyphs">PRESENT AN OFFER</text>
  <text class="stage-note on-red" x="540" y="905" font-size="16">-Which Provider?</text>

  <!-- band labels -->
  <g transform="rotate(51 1040 455)">
    <polyline points="1052,440 1040,455 1052,470" stroke="var(--white)" stroke-width="7" fill="none"/>
  </g>
  <g class="band-label" font-size="27" transform="rotate(51)">
  </g>
  <text class="band-label" font-size="27" transform="translate(1092,462) rotate(51)">PROBLEM &amp; SOLUTION</text>
  <text class="band-label" font-size="27" transform="translate(1064,490) rotate(51)">SUBJECT SHOWING SYMPTOMS</text>
  <text class="band-label" font-size="27" transform="translate(1036,516) rotate(51)">OF PROBLEM</text>

  <g transform="rotate(51 920 650)">
    <polyline points="932,635 920,650 932,665" stroke="var(--white)" stroke-width="7" fill="none"/>
  </g>
  <text class="band-label" font-size="27" transform="translate(973,650) rotate(51)">PROBLEM &amp; SOLUTION</text>
  <text class="band-label" font-size="27" transform="translate(945,678) rotate(51)">SUBJECT SHOWING SYMPTOMS</text>
  <text class="band-label" font-size="27" transform="translate(917,704) rotate(51)">OF PROBLEM</text>

  <g transform="rotate(51 780 910)">
    <polyline points="792,895 780,910 792,925" stroke="var(--white)" stroke-width="7" fill="none"/>
  </g>
  <text class="band-label" font-size="30" transform="translate(810,948) rotate(51)">CONVERT &amp; RETAIN</text>

  <!-- word of mouth arrow -->
  <line class="flow-arrow" x1="200" y1="512" x2="272" y2="634"/>
  <line class="flow-arrow" x1="455" y1="942" x2="540" y2="1085"/>
  <polyline class="flow-arrow" points="197,526 200,512 212,519"/>
  <polyline class="flow-arrow" points="528,1078 540,1085 541,1071"/>
  <text class="band-label" font-size="30" transform="translate(280,650) rotate(59.3)">WOM &amp; REFERRAL</text>

  <!-- site -->
  <text class="site-url" x="193" y="1224" font-size="34">kitefieldmedia.com.au</text>
</svg>
</body>
</html>
```